Product Label Redesign for a CBD Balm - 7.25" x 1.5"

We are redesigning our product label for a CBD balm to comply with federal standards and copyright issues. We are looking for designs that stand out on a shelf, but also have a professional look to them. Base color is flat black, with bright greens that pop out. Other colors are optional. We want to impart quality, but not look boring or medicinal. Attached is our current label (Harlow's Pick) and the sample label we used as a guide (Verda Leafe). Please design a label that would stand out among a shelf of various CBD balms. For more information PLEASE VISIT our website at https://harlowspick.example/.
Label dimensions are 7.25" x 1.5"
Thank you! - Gregory

Target Market(s)

General public.

Industry/Entity Type

CND balms and lotions.

Font styles to use
Sans Serif

Requirements
Must have
• ALL the content of the current label plus bar code. Size: 7.25" x 1.5"
Nice to have
• A design that really stands out on a shelf of CBD products. We are currently using flat black and bright green, but are open to other colors.
Should not have
• By law we cannot use the works "pain" or "relief" or any other similar words. We DO NOT want any association with marijuana as our product does not contain it--only CBD. So please no pot leaves.

```html
<!DOCTYPE html>
<html lang="en">
<head>
<meta charset="utf-8">
<title>Harlow's Pick – CBD Muscle &amp; Joint Blam Label</title>
<link rel="stylesheet" href="https://fonts.googleapis.com/css2?family=Montserrat:wght@600&family=Fira+Sans+Extra+Condensed:ital,wght@0,400;0,600;1,600&family=Passion+One:wght@400;700&display=swap">
<style>
  :root {
    --page: #ffffff;
    --label-black: #0b0b0b;
    --text-light: #f2f2f2;
    --lime: #a6d63a;
    --lime-bright: #c3ec52;
    --pill-grey: #d9d9d9;
    --code-white: #ffffff;
    --band-olive: #5f6a1e;
    --band-tan: #b99a56;
  }
  * { margin: 0; padding: 0; box-sizing: border-box; }
  html, body {
    width: 1200px; height: 1200px; overflow: hidden;
    background: var(--page);
  }
  .label {
    position: absolute;
    left: 40px; top: 484px;
    width: 1120px; height: 232px;
    background: var(--label-black);
    border-radius: 3px;
    color: var(--text-light);
    font-family: "Fira Sans Extra Condensed", sans-serif;
    font-size: 12.5px;
    line-height: 1.4;
    overflow: hidden;
  }
  .brand {
    position: absolute;
    display: flex; align-items: center; gap: 6px;
    font-family: "Montserrat", sans-serif;
    font-weight: 600;
    color: var(--text-light);
    white-space: nowrap;
  }
  .brand-square { display: inline-block; background: var(--lime); }
  .brand--info { left: 26px; top: 24px; font-size: 21px; }
  .brand--info .brand-square { width: 18px; height: 18px; }
  .brand--front { left: 648px; top: 14px; font-size: 15px; }
  .brand--front .brand-square { width: 13px; height: 13px; }

  .info-block { position: absolute; left: 26px; top: 60px; width: 222px; }
  .url-pill {
    display: block;
    margin: 4px 0 6px 14px;
    width: 191px; height: 19px;
    border-radius: 10px;
    background: var(--pill-grey);
    color: #1a1a1a;
    font-weight: 600;
    font-size: 14px;
    line-height: 19px;
    text-align: center;
  }
  .heading { font-style: italic; font-weight: 600; }
  .warning-text { letter-spacing: 0.4px; }

  .details-block { position: absolute; left: 310px; top: 22px; width: 262px; }
  .details-block p { margin-bottom: 4px; }

  .front-panel {
    position: absolute; left: 640px; top: 38px; width: 170px;
    text-align: center;
  }
  .product-mark {
    font-family: "Passion One", sans-serif;
    font-weight: 700;
    font-size: 86px;
    line-height: 0.82;
    color: var(--lime-bright);
    letter-spacing: 1px;
  }
  .product-name {
    font-family: "Passion One", sans-serif;
    font-size: 22px;
    line-height: 1.1;
    color: #d8d8d8;
    margin-top: 4px;
  }
  .strength-pill {
    display: inline-block;
    margin-top: 5px;
    width: 147px; height: 19px;
    border-radius: 10px;
    background: var(--lime);
    color: #111;
    font-weight: 600;
    font-size: 14px;
    line-height: 19px;
  }
  .net-contents {
    position: absolute; left: 673px; top: 196px; width: 106px;
    text-align: center; font-size: 12px; line-height: 1.2;
  }
  .net-contents .divider-square {
    display: inline-block; width: 10px; height: 10px;
    background: var(--lime); margin: 0 4px; vertical-align: -1px;
  }
  .origin { display: block; font-size: 8px; margin-top: 2px; }

  .claims { position: absolute; left: 880px; top: 22px; width: 222px; list-style: none; font-size: 13px; }
  .claims li { position: relative; padding-left: 16px; margin-bottom: 3px; }
  .claims li::before {
    content: ""; position: absolute; left: 2px; top: 6px;
    width: 8px; height: 8px; background: var(--lime);
  }

  .barcode-area {
    position: absolute; left: 911px; top: 119px;
    width: 155px; height: 72px;
    background: var(--code-white);
  }

  .pattern-band {
    position: absolute; top: 203px; height: 20px;
    background: linear-gradient(90deg, var(--band-olive), var(--lime), var(--band-tan), var(--lime), var(--band-olive));
  }
  .pattern-band--left { left: 0; width: 673px; }
  .pattern-band--right { left: 779px; width: 322px; }
</style>
</head>
<body>
  <section class="label">
    <div class="brand brand--info"><span class="brand-square"></span>Harlow's Pick</div>

    <div class="info-block">
      <p>To view our other products or repurchase, visit our website.</p>
      <span class="url-pill">www.harlowspick.example</span>
      <p class="heading">Warning:</p>
      <p class="warning-text">For external use only. Use only as directed. Keep away from eyes. Keep out reach of children.</p>
    </div>

    <div class="details-block">
      <p class="heading">Directions:</p>
      <p>Rub in a small amount over the affected area 3-4-time daily.</p>
      <p class="heading">Active Ingredient:</p>
      <p>Menthol 6%.</p>
      <p class="heading">Inactive Ingredient:</p>
      <p>Bees wax, olive oil, camphor, CBD hemp extract, CBN hemp extract, eucalyptus oil, clove oil, peppermint oil, tea tree oil, sorbic acid.</p>
    </div>

    <div class="brand brand--front"><span class="brand-square"></span>Harlow's Pick</div>

    <div class="front-panel">
      <div class="product-mark">CBD</div>
      <div class="product-name">MUSCLE &amp; JOINT<br>BLAM</div>
      <span class="strength-pill">500 MG PURE CBD</span>
    </div>

    <div class="net-contents">4 FL OZ<span class="divider-square"></span>118 ML<span class="origin">Made in Sonoma CA</span></div>

    <ul class="claims">
      <li>Long - lasting comfort for neck, back and muscle aches, including arthritis.</li>
      <li>Made from all-natural ingredients.</li>
      <li>Moisturizes skin while soothing it.</li>
    </ul>

    <div class="barcode-area" role="img" aria-label="Space reserved for the product barcode"></div>

    <div class="pattern-band pattern-band--left" role="img" aria-label="Decorative band of small green and tan tiles"></div>
    <div class="pattern-band pattern-band--right" role="img" aria-label="Decorative band of small green and tan tiles"></div>
  </section>
</body>
</html>
```